Brightwave Reach - Business Card

We need a business card for a Social Media Marketing company that specializes in online marketing for small businesses in Canada using common Social Media platforms such as Pictora, Kinloop, Blinkit & Chirpo.

I have uploaded a copy of our logo which I would like utilized in the business card. We would like the business card to be modern yet classy design.

Our website is www.brightwavereach.ca

Industry/Entity Type

Marketing

Contact Information for Business Card

Email: info@brightwavereach.ca
Website: www.brightwavereach.ca
Telephone: 604-392-5108

Colors

Designer to choose colors to be used in the design.

Requirements
Must have
• Social Media icons on reverse
• Please add some designs with color.

```html
<!DOCTYPE html>
<html lang="en">
<head>
<meta charset="utf-8">
<title>Brightwave Reach – Business Card</title>
<link rel="stylesheet" href="https://fonts.googleapis.com/css2?family=Roboto+Condensed:wght@400;700&family=Roboto:wght@400&display=swap">
<style>
  :root {
    --backdrop: #2a2a2a;
    --slate: #3d4144;
    --slate-edge: #33373a;
    --paper: #f1f1f1;
    --ink: #3a3e41;
    --muted: #a9abad;
    --white: #ffffff;
    --rule: #8e9194;
  }
  * { margin: 0; padding: 0; box-sizing: border-box; }
  html, body { width: 1200px; height: 960px; overflow: hidden; }
  body {
    background: var(--backdrop);
    position: relative;
    font-family: "Roboto", Arial, sans-serif;
  }
  .card { position: absolute; width: 600px; box-shadow: 0 6px 14px rgba(0,0,0,.55); }

  /* Front */
  .card-front { left: 314px; top: 113px; height: 342px; background: var(--paper); }
  .front-band { position: absolute; left: 0; top: 0; width: 100%; height: 102px; background: var(--slate); }
  .front-edge { position: absolute; left: 0; bottom: 0; width: 100%; height: 12px; background: var(--slate-edge); }
  .front-wordmark {
    position: absolute; left: 235px; top: 47px; width: 130px; height: 125px;
    background: var(--paper);
    display: flex; align-items: center; justify-content: center; text-align: center;
    font-family: "Roboto Condensed", Arial, sans-serif; font-weight: 700;
    font-size: 21px; line-height: 1.15; color: var(--ink); text-transform: uppercase;
    white-space: nowrap;
  }
  .person { position: absolute; left: 0; top: 215px; width: 100%; text-align: center; }
  .person-name {
    font-family: "Roboto Condensed", Arial, sans-serif; font-weight: 700;
    font-size: 21px; color: var(--ink); letter-spacing: .3px;
  }
  .person-title {
    font-family: "Roboto Condensed", Arial, sans-serif; font-size: 15px;
    color: var(--muted); margin-top: 2px;
  }
  .contact { position: absolute; left: 0; width: 100%; display: flex; justify-content: center; gap: 10px;
    font-size: 14px; color: var(--ink); }
  .contact-row-1 { top: 271px; }
  .contact-row-2 { top: 290px; }
  .contact-item { display: inline-flex; align-items: center; gap: 4px; }
  .contact-item svg { width: 12px; height: 12px; fill: var(--ink); }

  /* Back */
  .card-back { left: 311px; top: 472px; height: 342px; background: var(--slate); }
  .back-wordmark {
    position: absolute; left: 0; top: 100px; width: 100%; text-align: center;
    font-family: "Roboto Condensed", Arial, sans-serif; font-weight: 700;
    font-size: 36px; line-height: 1.1; color: var(--white); text-transform: uppercase;
  }
  .social-row { position: absolute; left: 0; top: 289px; width: 100%;
    display: flex; align-items: center; justify-content: center; gap: 10px; }
  .social-rule { width: 125px; height: 1px; background: linear-gradient(90deg, transparent, var(--rule)); }
  .social-rule.right { background: linear-gradient(90deg, var(--rule), transparent); }
  .social-item { display: inline-flex; align-items: center; gap: 4px;
    font-family: "Roboto Condensed", Arial, sans-serif; font-size: 13px; color: var(--white); }
  .social-item .dot { width: 12px; height: 12px; border: 1.5px solid var(--white); border-radius: 50%; }
</style>
</head>
<body>
  <section class="card card-front">
    <div class="front-band"></div>
    <div class="front-wordmark">Brightwave<br>Reach</div>
    <div class="person">
      <div class="person-name">DANIEL REYES</div>
      <div class="person-title">CEO/FOUNDER</div>
    </div>
    <div class="contact contact-row-1">
      <span class="contact-item">
        <svg viewBox="0 0 24 24"><path d="M6.6 10.8a15.1 15.1 0 0 0 6.6 6.6l2.2-2.2a1 1 0 0 1 1-.25 11.4 11.4 0 0 0 3.6.57 1 1 0 0 1 1 1V20a1 1 0 0 1-1 1A17 17 0 0 1 3 4a1 1 0 0 1 1-1h3.5a1 1 0 0 1 1 1c0 1.25.2 2.45.57 3.570a1 1 0 0 1-.25 1z"/></svg>
        604-392-5108
      </span>
      <span class="contact-item">
        <svg viewBox="0 0 24 24"><path d="M2 5h20v14H2z M2 5l10 8 10-8" fill="none" stroke="#3a3e41" stroke-width="2.5"/><path d="M2 5h20L12 12z"/></svg>
        info@brightwavereach.ca
      </span>
    </div>
    <div class="contact contact-row-2">
      <span class="contact-item">
        <svg viewBox="0 0 24 24"><circle cx="12" cy="12" r="10"/><path d="M2 12h20M12 2c3 3 3 17 0 20M12 2c-3 3-3 17 0 20" fill="none" stroke="#f1f1f1" stroke-width="1.5"/></svg>
        www.brightwavereach.ca
      </span>
    </div>
    <div class="front-edge"></div>
  </section>

  <section class="card card-back">
    <div class="back-wordmark">Brightwave<br>Reach</div>
    <div class="social-row">
      <span class="social-rule"></span>
      <span class="social-item"><span class="dot"></span>Kinloop</span>
      <span class="social-item"><span class="dot"></span>Pictora</span>
      <span class="social-item"><span class="dot"></span>Chirpo</span>
      <span class="social-rule right"></span>
    </div>
  </section>
</body>
</html>
```